First North America Product Category Rule

8 x 10 foot booth design for a stretch fabric wrap-around. The booth will be used in a very small exhibit area for 150 attendees. It is for the packaging industry focused on the environment. This booth graphic is NOT about our company, but to promote participation in a project we are sponsoring. The project is to develop the first North American Packaging Category Rule, so the booth is to invite conference attendees to join our effort. Production specifications are attached.

Target Market(s)

Meridian 300, Sustainability Directors, Packaging Engineers

Industry/Entity Type

Packaging; Environment

Font styles to use
Sans Serif

Requirements
Must have
• An Eye-Catching or Intriguing Image/Graphics/Letter Treatment
Should not have
• Nothing too bright or garish. All text should be above waist height (No text below the 36-40" mark)

```html
<!DOCTYPE html>
<html lang="en">
<head>
<meta charset="utf-8">
<title>First North American PCR for Protective Packaging – Booth Graphic</title>
<link href="https://fonts.googleapis.com/css2?family=Barlow:wght@400;500;600;700&display=swap" rel="stylesheet">
<style>
  :root {
    --stage: #95aaac;
    --paper: #ffffff;
    --orange: #e25226;
    --orange-deep: #c9441c;
    --ink: #111111;
    --line-faint: #ececec;
    --shirt: #5f86b8;
    --shirt-light: #8fb0d6;
    --hall-dark: #3a2a20;
    --hall-warm: #b07a48;
  }
  * { box-sizing: border-box; margin: 0; padding: 0; }
  html, body { width: 857px; height: 1200px; overflow: hidden; }
  body {
    background: var(--stage);
    font-family: "Barlow", Arial, sans-serif;
    position: relative;
  }
  .banner {
    position: absolute;
    left: 28px; top: 374px;
    width: 800px; height: 451px;
    background: var(--paper);
    overflow: hidden;
    box-shadow: 0 14px 22px rgba(0,0,0,0.18);
  }
  .banner-art { position: absolute; inset: 0; width: 100%; height: 100%; }
  .kicker {
    position: absolute; left: 150px; top: 46px;
    color: var(--orange); font-size: 14px; font-weight: 400; letter-spacing: 0.1px;
  }
  .headline {
    position: absolute; left: 150px; top: 63px;
    color: var(--ink); font-size: 25px; font-weight: 700; line-height: 27px;
    text-transform: uppercase;
  }
  .headline .accent { color: var(--orange); font-weight: 400; }
  .subhead {
    position: absolute; left: 150px; top: 127px;
    color: var(--ink); font-size: 16.5px; font-weight: 700;
  }
  .steps {
    position: absolute; left: 151px; top: 160px;
    width: 210px; height: 80px;
    display: grid; grid-template-columns: 101px 109px; grid-template-rows: 39px 41px;
  }
  .step { font-size: 8.6px; line-height: 10px; color: var(--ink); padding-top: 3px; }
  .step:nth-child(2n) { padding-left: 6px; border-left: 1px solid var(--orange); }
  .step:nth-child(-n+2) { border-bottom: 1px solid var(--orange); }
  .step .num { display: block; color: var(--orange); font-weight: 700; }
  .step .gap { display: block; height: 10px; }
  .credits {
    position: absolute; left: 151px; top: 252px;
    color: var(--orange); font-size: 8.6px; font-weight: 700; line-height: 10px;
  }
  .quote {
    position: absolute; left: 391px; top: 160px;
    width: 170px; height: 79px;
    background: var(--orange);
    border-radius: 6px 0 0 6px;
    color: #fff; font-size: 8.3px; font-weight: 700; line-height: 9.6px;
    padding: 6px 8px; text-transform: uppercase;
  }
  .signup {
    position: absolute; left: 561px; top: 28px;
    width: 89px; height: 37px;
    border: 3px solid var(--orange); border-radius: 7px;
    color: var(--orange); font-size: 22px; font-weight: 700; line-height: 30px;
    text-align: center; letter-spacing: -0.5px;
  }
</style>
</head>
<body>
  <section class="banner">
    <svg class="banner-art" viewBox="0 0 1273 718" preserveAspectRatio="none" aria-hidden="false">
      <defs>
        <linearGradient id="hall" x1="0" y1="0" x2="1" y2="0">
          <stop offset="0" stop-color="var(--hall-dark)"/>
          <stop offset="0.5" stop-color="var(--hall-warm)"/>
          <stop offset="1" stop-color="var(--hall-dark)"/>
        </linearGradient>
        <linearGradient id="shirt" x1="0" y1="0" x2="0" y2="1">
          <stop offset="0" stop-color="#efe8e2"/>
          <stop offset="0.35" stop-color="var(--shirt-light)"/>
          <stop offset="1" stop-color="var(--shirt)"/>
        </linearGradient>
      </defs>
      <!-- faint decorative outlines -->
      <g class="outline-deco" fill="none" stroke="var(--line-faint)" stroke-width="16">
        <path d="M120 0 C200 20 240 80 280 180 L320 320 C360 440 330 520 240 600"/>
        <path d="M1080 150 C1040 150 1020 190 1000 240 L960 330 C940 380 940 420 960 470 L1000 560 C1020 610 1040 680 1100 680 L1273 680"/>
        <path d="M1273 425 L1180 425 C1140 425 1120 440 1100 470"/>
        <path d="M880 0 L940 90 L1040 90 L1100 0"/>
      </g>
      <!-- left orange shape -->
      <path class="shape-orange" fill="var(--orange)" d="M0 158 L150 420 C210 520 230 600 190 718 L0 718 Z"/>
      <path fill="var(--orange)" d="M210 718 C260 690 320 675 370 672 L360 718 Z"/>
      <!-- right orange shape -->
      <path class="shape-orange" fill="var(--orange)" d="M1175 0 L1273 0 L1273 378 C1240 370 1215 345 1185 290 L1140 205 C1115 155 1115 110 1140 65 Z"/>
      <!-- orange band above hall -->
      <path fill="var(--orange)" d="M330 718 C400 580 440 440 620 440 L820 440 L1120 600 L1180 718 Z"/>
      <!-- hall photo area -->
      <path role="img" aria-label="Blurred warehouse aisle with stacked packaging" fill="url(#hall)" d="M360 718 C430 600 470 470 640 468 L800 468 L800 718 Z"/>
      <!-- person photo area -->
      <path role="img" aria-label="Smiling engineer in white hard hat and blue shirt, arms crossed" fill="url(#shirt)" d="M760 718 L760 330 C790 250 840 200 930 170 C1010 190 1060 250 1130 320 L1130 718 Z"/>
      <!-- sign-up pointer -->
      <g class="pointer-icon" fill="none" stroke="var(--orange)" stroke-width="5" stroke-linecap="round" stroke-linejoin="round">
        <path d="M950 110 L950 150 M950 150 C960 140 968 140 972 150 M972 150 C980 140 988 140 992 152 M992 152 C1000 146 1008 148 1010 160 L1010 170 C1010 182 1000 190 990 190 L960 190 C950 185 935 170 930 160 C926 152 934 146 942 152 L950 160"/>
        <path d="M1000 195 L1010 200"/>
      </g>
    </svg>

    <p class="kicker">FIRST NORTH AMERICAN</p>
    <h1 class="headline">Product Category Rule <span class="accent">(PCR)</span><br>For Protective Packaging</h1>
    <h2 class="subhead">ENLISTING STAKEHOLDER PARTICIPATION</h2>

    <div class="steps">
      <div class="step"><span class="num">01.</span>PCR<br>Product Category Rules</div>
      <div class="step"><span class="num">02.</span>LCA<br>Life Cycle Assessment</div>
      <div class="step"><span class="num">03.</span><span class="gap"></span>Third Party Verification</div>
      <div class="step"><span class="num">04.</span>EPD<br>Registration &amp; Publication</div>
    </div>

    <p class="credits">Sponsored by Foam Pack Coalition<br>Managed by Open Ledger Works</p>

    <blockquote class="quote">“How EPD can move<br>the dialogue beyond<br>end-of-life disposal<br>to include environmental<br>benchmarks for<br>product production<br>&amp; distribution”</blockquote>

    <div class="signup">SIGN UP</div>
  </section>
</body>
</html>
```